M Zyvantics Buisness Cards

I need a technology focused clean business card for my employees. I have attached out logo to include in the mocks. We're a modern tech consulting firm that drives to interface humanity with technology in a truly cohesive fashion.

```html
<!DOCTYPE html>
<html lang="en">
<head>
<meta charset="utf-8">
<title>M Zyvantics Business Cards</title>
<link href="https://fonts.googleapis.com/css2?family=Lato:wght@400;700&display=swap" rel="stylesheet">
<style>
  :root {
    --bg: #2b2d30;
    --blue-deep: #1565b8;
    --blue-light: #2a90dd;
    --ink: #242526;
    --white: #ffffff;
  }
  * { margin: 0; padding: 0; box-sizing: border-box; }
  html, body {
    width: 1200px; height: 900px; overflow: hidden;
    background: var(--bg);
    font-family: "Lato", sans-serif;
  }
  .canvas { position: relative; width: 1200px; height: 900px; }
  .card {
    position: absolute; top: 300px;
    width: 525px; height: 300px;
    border-radius: 24px; overflow: hidden;
    box-shadow: 0 18px 40px rgba(0,0,0,.45);
  }
  .card--info {
    left: 50px;
    background: linear-gradient(135deg, var(--blue-deep), var(--blue-light));
  }
  .info-band { position: absolute; inset: 0; width: 525px; height: 300px; }
  .brand {
    position: absolute; display: flex; align-items: center; gap: 10px;
    color: var(--white); font-weight: 700; letter-spacing: .5px;
  }
  .brand__dot { border-radius: 50%; border: 3px solid var(--blue-light); }
  .card--info .brand { left: 32px; top: 32px; font-size: 24px; }
  .card--info .brand__dot { width: 28px; height: 28px; }
  .holder {
    position: absolute; right: 50px; top: 140px; text-align: right;
  }
  .holder__name {
    color: var(--white); font-size: 24px; font-weight: 700; line-height: 1;
  }
  .holder__role {
    color: var(--ink); font-size: 16px; line-height: 1.1; margin-top: 3px;
  }
  .contacts {
    position: absolute; left: 34px; top: 180px; list-style: none;
    color: var(--white); font-size: 12px; line-height: 19px;
  }
  .contacts li { display: flex; align-items: center; gap: 8px; }
  .contacts svg { width: 12px; height: 12px; flex: none; }
  .address {
    position: absolute; right: 50px; bottom: 22px; text-align: right;
    color: var(--white); font-size: 15px; font-weight: 700; line-height: 1.35;
  }
  .card--logo {
    left: 625px;
    background: radial-gradient(circle at 55% 70%, var(--blue-light), var(--blue-deep) 80%);
  }
  .card--logo .brand {
    inset: 0; justify-content: center; font-size: 44px; gap: 16px;
  }
  .card--logo .brand__dot { width: 46px; height: 46px; border-color: var(--white); }
</style>
</head>
<body>
<main class="canvas">

  <section class="card card--info" aria-label="Business card, contact side">
    <svg class="info-band" viewBox="0 0 525 300" aria-hidden="true">
      <path d="M0 0 H525 V128 L410 123 L399 137 L388 122 L0 104 Z" fill="var(--ink)"/>
      <line x1="40" y1="150" x2="480" y2="196" stroke="var(--white)" stroke-width="1.5"/>
    </svg>

    <div class="brand"><span class="brand__dot"></span>M Zyvantics</div>

    <div class="holder">
      <p class="holder__name">Person’s Name</p>
      <p class="holder__role">Funder</p>
    </div>

    <ul class="contacts">
      <li>
        <svg viewBox="0 0 24 24"><path fill="currentColor" d="M6.6 10.8a15.1 15.1 0 0 0 6.6 6.6l2.2-2.2c.3-.3.7-.4 1-.2 1.1.4 2.3.6 3.6.6.6 0 1 .4 1 1V20c0 .6-.4 1-1 1A17 17 0 0 1 3 4c0-.6.4-1 1-1h3.5c.6 0 1 .4 1 1 0 1.3.2 2.5.6 3.6.1.3 0 .7-.2 1z"/></svg>
        (555)014-2276
      </li>
      <li>
        <svg viewBox="0 0 24 24"><path fill="currentColor" d="M2 5h20v14H2z"/><path d="M3 6l9 7 9-7" fill="none" stroke="#1a6fc2" stroke-width="1.8"/></svg>
        hello@mzyvanticsgroup.com
      </li>
      <li>
        <svg viewBox="0 0 24 24"><g fill="none" stroke="currentColor" stroke-width="2"><circle cx="12" cy="12" r="10"/><path d="M2 12h20M12 2c3 3 3 17 0 20M12 2c-3 3-3 17 0 20"/></g></svg>
        www.mzyvanticsgroup.com
      </li>
    </ul>

    <p class="address">P.O Box 200418 Austin<br>Texas 78701</p>
  </section>

  <section class="card card--logo" aria-label="Business card, brand side">
    <div class="brand"><span class="brand__dot"></span>M Zyvantics</div>
  </section>

</main>
</body>
</html>
```